Company Mission & Values Poster

I'd like an A2 Portrait Poster displaying our company's Mission & Values.
See our website for our logo, fonts, mission & values.
https://talvendo.com.au/

Our Mission: Creating homes for abundant life
Values: Love, Thinking, Team, Zoe.

Some ideas to consider:
Mission as the Headline then
A logo for each of the 4 Values and the words

Target Market(s)

Myself & my team

Industry/Entity Type

Real Estate

Font styles to use
Other font styles liked:
• Company fonts as seen on our website

```html
<!DOCTYPE html>
<html lang="en">
<head>
<meta charset="utf-8">
<title>Talvendo – Mission &amp; Values Poster</title>
<link rel="stylesheet" href="https://fonts.googleapis.com/css2?family=Playfair+Display:wght@500;700;800&family=Montserrat:wght@400;500&display=swap">
<style>
  :root {
    --backdrop: #a9c3bf;
    --paper: #ffffff;
    --ink: #161616;
    --forest: #0b3d35;
    --forest-deep: #08322b;
    --teal: #2e7d6c;
    --teal-light: #347f70;
    --pill: #f1f2f1;
    --pill-edge: #dfe3e1;
    --divider: #5f9b8d;
  }
  html, body {
    margin: 0;
    padding: 0;
    width: 1200px;
    height: 2400px;
    overflow: hidden;
    background: var(--backdrop);
  }
  .poster {
    position: absolute;
    left: 50px;
    top: 421px;
    width: 1100px;
    height: 1558px;
    box-shadow: 0 18px 40px rgba(0, 0, 0, 0.28);
    display: block;
  }
  .brand-name {
    font-family: "Playfair Display", serif;
    font-weight: 500;
    fill: var(--forest);
    letter-spacing: 14px;
  }
  .mission-our {
    font-family: "Playfair Display", serif;
    font-weight: 800;
    fill: var(--forest);
  }
  .mission-label {
    font-family: "Playfair Display", serif;
    font-weight: 700;
    fill: var(--forest);
    letter-spacing: 1px;
  }
  .headline {
    font-family: "Playfair Display", serif;
    font-weight: 700;
    fill: var(--ink);
  }
  .mission-body {
    font-family: "Montserrat", sans-serif;
    font-weight: 500;
    fill: var(--ink);
  }
  .value-title {
    font-family: "Playfair Display", serif;
    font-weight: 700;
  }
  .value-title--dark { fill: var(--forest); }
  .value-title--teal { fill: var(--teal); }
  .value-body {
    font-family: "Montserrat", sans-serif;
    font-weight: 400;
    fill: var(--ink);
  }
  .values-heading {
    font-family: "Playfair Display", serif;
    font-weight: 800;
    fill: var(--paper);
  }
</style>
</head>
<body>
<svg class="poster" viewBox="0 0 865 1225" xmlns="http://www.w3.org/2000/svg">
  <defs>
    <linearGradient id="forest-band" x1="0" y1="1" x2="1" y2="0">
      <stop offset="0" stop-color="#08332c"/>
      <stop offset="0.55" stop-color="#135246"/>
      <stop offset="1" stop-color="#2e7d6c"/>
    </linearGradient>
    <linearGradient id="pill-fill" x1="0" y1="0" x2="0" y2="1">
      <stop offset="0" stop-color="#fafbfa"/>
      <stop offset="1" stop-color="#e7eae8"/>
    </linearGradient>
    <filter id="pill-shadow" x="-10%" y="-30%" width="120%" height="160%">
      <feDropShadow dx="0" dy="4" stdDeviation="5" flood-color="#000" flood-opacity="0.3"/>
    </filter>
    <clipPath id="poster-clip">
      <rect width="865" height="1225"/>
    </clipPath>
  </defs>

  <g clip-path="url(#poster-clip)">
    <!-- paper -->
    <rect class="paper" width="865" height="1225" fill="var(--paper)"/>

    <!-- brand -->
    <text class="brand-name" x="432" y="160" font-size="82" text-anchor="middle">TALVENDO</text>

    <!-- green values band -->
    <rect class="values-band" x="0" y="519" width="865" height="706" fill="url(#forest-band)"/>

    <!-- mission medallion -->
    <circle class="mission-disc" cx="88" cy="409" r="192" fill="var(--paper)"/>
    <path class="mission-ring-outer" d="M 56 225 A 186 186 0 1 1 56 593" fill="none" stroke="var(--ink)" stroke-width="4"/>
    <path class="mission-ring-inner" d="M 100 247 A 150 150 0 0 1 100 547" fill="none" stroke="var(--teal)" stroke-width="4"/>
    <text class="mission-our" x="114" y="400" font-size="74" text-anchor="middle">OUR</text>
    <text class="mission-label" x="114" y="437" font-size="37" text-anchor="middle">MISSION</text>

    <!-- mission statement -->
    <text class="headline" x="306" y="314" font-size="47">CREATING HOMES</text>
    <text class="headline" x="306" y="360" font-size="47">FOR ABUNDANT LIFE</text>
    <text class="mission-body" font-size="17.2">
      <tspan x="306" y="401">We wholeheartedly believe that home is an extraordinary</tspan>
      <tspan x="306" y="422">place: a haven where life unfolds in all its glory. Where we</tspan>
      <tspan x="306" y="443">find solace, make cherished memories with loved ones,</tspan>
      <tspan x="306" y="464">and savour the  natural beauty that surrounds us.</tspan>
    </text>

    <!-- values arcs -->
    <circle class="values-ring" cx="832" cy="872" r="272" fill="none" stroke="#111" stroke-width="4"/>
    <path class="values-ring-inner" d="M 805 650 A 225 225 0 0 0 805 1094" fill="none" stroke="var(--paper)" stroke-width="3"/>

    <text class="values-heading" transform="translate(722 900) rotate(-90)" font-size="72" text-anchor="middle">OUR</text>
    <text class="values-heading" transform="translate(786 900) rotate(-90)" font-size="84" text-anchor="middle">VALUES</text>

    <!-- value: Love -->
    <g class="value value--love">
      <rect x="28" y="610" width="630" height="105" rx="52" fill="url(#pill-fill)" filter="url(#pill-shadow)"/>
      <line x1="218" y1="630" x2="218" y2="696" stroke="var(--divider)" stroke-width="1.2" stroke-dasharray="2 3"/>
      <text class="value-title value-title--dark" x="131" y="672" font-size="32" text-anchor="middle">Love</text>
      <text class="value-body" font-size="13.6">
        <tspan x="232" y="645">Our mission is founded in our love and respect</tspan>
        <tspan x="232" y="661">for people – those we develop for, those in our</tspan>
        <tspan x="232" y="677">teams and those in the communities we create</tspan>
        <tspan x="232" y="693">and operate within.</tspan>
      </text>
      <circle cx="666" cy="662" r="52" fill="var(--forest)" stroke="var(--paper)" stroke-width="3" role="img" aria-label="Icon: heart held by crossed arms"/>
    </g>

    <!-- value: Thinking -->
    <g class="value value--thinking">
      <rect x="28" y="748" width="540" height="105" rx="52" fill="url(#pill-fill)" filter="url(#pill-shadow)"/>
      <line x1="218" y1="768" x2="218" y2="834" stroke="var(--divider)" stroke-width="1.2" stroke-dasharray="2 3"/>
      <text class="value-title value-title--teal" x="131" y="811" font-size="32" text-anchor="middle">Thinking</text>
      <text class="value-body" font-size="13.6">
        <tspan x="232" y="773">We believe in the power of thinking. Our</tspan>
        <tspan x="232" y="789">rigorous and creative processes create</tspan>
        <tspan x="232" y="805">beautifully considered solutions for our</tspan>
        <tspan x="232" y="821">purchasers, the communities we develop</tspan>
        <tspan x="232" y="837">within and the environment.</tspan>
      </text>
      <circle cx="572" cy="800" r="50" fill="var(--teal)" stroke="var(--paper)" stroke-width="3" role="img" aria-label="Icon: brain inside a light bulb"/>
    </g>

    <!-- value: Team -->
    <g class="value value--team">
      <rect x="28" y="889" width="575" height="105" rx="52" fill="url(#pill-fill)" filter="url(#pill-shadow)"/>
      <line x1="218" y1="909" x2="218" y2="975" stroke="var(--divider)" stroke-width="1.2" stroke-dasharray="2 3"/>
      <text class="value-title value-title--dark" x="131" y="953" font-size="32" text-anchor="middle">Team</text>
      <text class="value-body" font-size="13.6">
        <tspan x="232" y="913">Property development is a team sport.</tspan>
        <tspan x="232" y="929">We surround ourselves with the best</tspan>
        <tspan x="232" y="945">designers and advisers. We strive to</tspan>
        <tspan x="232" y="961">create an environment that allows them</tspan>
        <tspan x="232" y="977">to do their best work and love doing it.</tspan>
      </text>
      <circle cx="559" cy="942" r="50" fill="var(--forest)" stroke="var(--paper)" stroke-width="3" role="img" aria-label="Icon: connected team of people"/>
    </g>

    <!-- value: Zoe -->
    <g class="value value--zoe">
      <rect x="28" y="1029" width="630" height="105" rx="52" fill="url(#pill-fill)" filter="url(#pill-shadow)"/>
      <line x1="218" y1="1049" x2="218" y2="1115" stroke="var(--divider)" stroke-width="1.2" stroke-dasharray="2 3"/>
      <text class="value-title value-title--teal" x="131" y="1093" font-size="32" text-anchor="middle">Zoe</text>
      <text class="value-body" font-size="13.6">
        <tspan x="232" y="1053">Our mission is to create places for</tspan>
        <tspan x="232" y="1069">‘Zoe’ – the Greek word for abundant life.</tspan>
        <tspan x="232" y="1085">We do this through exquisite design,</tspan>
        <tspan x="232" y="1101">quality construction and celebrating</tspan>
        <tspan x="232" y="1117">nature.</tspan>
      </text>
      <circle cx="651" cy="1082" r="52" fill="var(--teal)" stroke="var(--paper)" stroke-width="3" role="img" aria-label="Icon: open hands holding a heart"/>
    </g>
  </g>
</svg>
</body>
</html>
```